Signage for Multi-family Veterans Housing community

Need a design concept package for the above. Need Historic feel design logo element together with "Ashcombe Veterans Village"in serif font, for a Veterans (retired military) Affordable Housing community, in the historic town of Windsor, California USA. I have attached an architectural drawing of the future housing community, that will need the signage. Also, attached are photos of the town of Windsor signage, for the historic downtown vibe, do not use the sign elements. Please include in the concept package a community ID sign similar to the craftsman community ID sign attached. The community ID sign will have the logo with name and address only, use a placeholder for Address. Thank you

Font styles to use
Serif
Sans Serif

Requirements
Should not have
• Please no American flags or other military references. Other than the word “I Veterans” in the title.

```html
<!DOCTYPE html>
<html lang="en">
<head>
<meta charset="utf-8">
<title>Ashcombe Veterans Village – Community ID Sign</title>
<link href="https://fonts.googleapis.com/css2?family=Playfair+Display:wght@700;800&family=Playfair+Display+SC:wght@700&family=Montserrat:wght@400;500&display=swap" rel="stylesheet">
<style>
  :root {
    --sign-red: #930000;
    --sign-white: #ffffff;
    --ornament-tone: #b23a3a;
    --backdrop: #efedea;
  }
  html, body {
    margin: 0;
    padding: 0;
    width: 1200px;
    height: 981px;
    overflow: hidden;
    background: var(--backdrop);
  }
  .sign {
    position: absolute;
    left: 43px;
    top: 98px;
    width: 1113px;
    height: 784px;
    background: var(--sign-red);
    color: var(--sign-white);
  }
  .sign-frame {
    position: absolute;
    inset: 26px;
    border: 2px solid var(--sign-white);
  }
  .sign-line {
    position: absolute;
    left: 0;
    right: 0;
    margin: 0;
    text-align: center;
    line-height: 1;
    white-space: nowrap;
  }
  .community-name {
    top: 86px;
    font-family: "Playfair Display", serif;
    font-weight: 800;
    font-size: 132px;
    letter-spacing: 0.12em;
    padding-left: 0.12em;
  }
  .community-type {
    top: 236px;
    font-family: "Playfair Display", serif;
    font-weight: 700;
    font-size: 70px;
    letter-spacing: 0.01em;
  }
  .laurel-ornament {
    position: absolute;
    top: 334px;
    left: 349px;
    width: 414px;
    height: 52px;
    background: var(--ornament-tone);
    border-radius: 26px;
  }
  .audience-band {
    position: absolute;
    top: 445px;
    left: 148px;
    width: 817px;
    height: 58px;
    background: var(--sign-white);
    color: var(--sign-red);
    font-family: "Montserrat", sans-serif;
    font-weight: 500;
    font-size: 33px;
    display: flex;
    align-items: center;
    justify-content: center;
    white-space: nowrap;
  }
  .housing-tagline {
    top: 520px;
    font-family: "Playfair Display SC", serif;
    font-weight: 700;
    font-size: 36px;
    letter-spacing: 0.02em;
  }
  .section-divider {
    position: absolute;
    top: 606px;
    left: 447px;
    width: 218px;
    height: 18px;
  }
  .town-line {
    top: 656px;
    font-family: "Montserrat", sans-serif;
    font-weight: 500;
    font-size: 41px;
    letter-spacing: 0.01em;
  }
</style>
</head>
<body>
  <section class="sign" aria-label="Ashcombe Veterans Village community ID sign">
    <div class="sign-frame"></div>
    <h1 class="sign-line community-name">Ashcombe</h1>
    <p class="sign-line community-type">VETERANS VILLAGE</p>
    <div class="laurel-ornament" role="img" aria-label="Pair of laurel sprigs ornament"></div>
    <div class="audience-band">FOR A VETERANS (RETIRED MILITARY)</div>
    <p class="sign-line housing-tagline">Affordable Housing Community</p>
    <svg class="section-divider" viewBox="0 0 218 18" aria-hidden="true">
      <line x1="14" y1="9" x2="204" y2="9" stroke="#ffffff" stroke-width="3" stroke-linecap="round"/>
      <polyline points="2,3 10,9 2,15" fill="none" stroke="#ffffff" stroke-width="2"/>
      <polyline points="216,3 208,9 216,15" fill="none" stroke="#ffffff" stroke-width="2"/>
    </svg>
    <p class="sign-line town-line">Historic town of Windsor, California USA</p>
  </section>
</body>
</html>
```